Design a cover for a new book!

Design a cover for a new book called "The Ledger and the Lathe" Subtitle is "A Fresh Monetary Blueprint Built For Modern Working Households"

The brief attached will give you the theme of the book. The book tells how there are two economies, one controlled by people who own financial assets, and the other run by people who build real things that contribute to our standard of living.

We want a split cover showing two different economies existing at the same time. The cover should show a split scene! Half the cover should be the monetary economy - the stock market or derivative or commodities. The other half the cover should show the material economy - technology and manufacturing, or maybe people living and doing things.

Target Market(s)

General Audience, people who like political policy

Industry/Entity Type

economics

Requirements
Must have
• The cover should show a split scene! Half the cover should be the monetary economy - the stock market or derivative or commodities. The other half the cover should show the material economy - technology and manufacturing,

```html
<!DOCTYPE html>
<html lang="en">
<head>
<meta charset="utf-8">
<title>The Ledger and the Lathe — Cover</title>
<link href="https://fonts.googleapis.com/css2?family=Lato:wght@400;700;900&display=swap" rel="stylesheet">
<style>
  :root {
    --page: #ffffff;
    --crimson: #c0143e;
    --paper: #f4f1ee;
    --ink-light: #ffffff;
    --money-blue: #3a4fa0;
    --money-violet: #4a2f8a;
    --money-night: #1e1f5c;
    --money-pale: #c9d3ec;
    --chart-cyan: #5fe3ff;
    --chart-blue: #3fa2ff;
    --chart-grid: rgba(160, 200, 255, 0.18);
    --factory-dark: #1d2633;
    --factory-steel: #4a5a6e;
    --robot-yellow: #f0b323;
    --work-blue: #2b4a78;
  }
  * { margin: 0; padding: 0; box-sizing: border-box; }
  html, body {
    width: 1200px; height: 1200px; overflow: hidden;
    background: var(--page);
  }
  .canvas {
    position: relative; width: 1200px; height: 1200px;
    background: var(--page);
  }
  .book-cover {
    position: absolute; left: 267px; top: 100px;
    width: 667px; height: 1000px; overflow: hidden;
    background: var(--crimson);
    font-family: 'Lato', sans-serif;
  }
  .scene-markets {
    position: absolute; left: 0; top: 0; width: 100%; height: 340px;
    background:
      radial-gradient(ellipse 220px 180px at 22% 40%, var(--money-pale) 0%, rgba(201,211,236,0) 100%),
      radial-gradient(ellipse 200px 160px at 75% 60%, rgba(220,60,160,0.45) 0%, rgba(220,60,160,0) 100%),
      linear-gradient(120deg, var(--money-blue) 0%, var(--money-violet) 55%, var(--money-night) 100%);
  }
  .market-chart {
    position: absolute; left: 0; top: 0; width: 667px; height: 340px;
  }
  .market-chart .grid line { stroke: var(--chart-grid); stroke-width: 1; }
  .market-chart .candle rect { fill: var(--chart-cyan); }
  .market-chart .candle line { stroke: var(--chart-cyan); stroke-width: 2; }
  .market-chart .candle--alt rect { fill: var(--chart-blue); }
  .market-chart .candle--alt line { stroke: var(--chart-blue); }
  .market-chart .trend { fill: none; stroke: rgba(255,255,255,0.55); stroke-width: 2; }

  .scene-industry {
    position: absolute; left: 0; top: 672px; width: 100%; height: 328px;
    background:
      radial-gradient(ellipse 110px 150px at 44% 62%, rgba(240,179,35,0.85) 0%, rgba(240,179,35,0) 100%),
      radial-gradient(ellipse 90px 150px at 66% 64%, rgba(240,179,35,0.8) 0%, rgba(240,179,35,0) 100%),
      radial-gradient(ellipse 80px 140px at 88% 62%, rgba(240,179,35,0.75) 0%, rgba(240,179,35,0) 100%),
      radial-gradient(ellipse 130px 220px at 14% 72%, var(--work-blue) 0%, rgba(43,74,120,0) 100%),
      radial-gradient(ellipse 200px 80px at 80% 8%, rgba(255,200,120,0.6) 0%, rgba(255,200,120,0) 100%),
      linear-gradient(180deg, var(--factory-steel) 0%, var(--factory-dark) 100%);
  }
  .torn-band {
    position: absolute; left: 0; top: 0; width: 100%; height: 100%;
  }
  .cover-text {
    position: absolute; left: 0; width: 100%;
    text-align: center; color: var(--ink-light);
  }
  .title-line {
    font-size: 56px; line-height: 1; letter-spacing: 0.5px;
    text-transform: uppercase;
  }
  .title-line--one { top: 368px; font-weight: 400; }
  .title-line--two { top: 433px; font-weight: 700; }
  .subtitle {
    top: 490px; font-size: 27px; font-weight: 400; line-height: 39px;
  }
  .author {
    top: 622px; font-size: 34px; line-height: 1; font-weight: 700;
    letter-spacing: 0.5px; text-transform: uppercase;
  }
</style>
</head>
<body>
<div class="canvas">
  <div class="book-cover">
    <div class="scene-markets" role="img" aria-label="Engraved banknote portrait in blue and violet tones behind a glowing stock market chart"></div>

    <svg class="market-chart" viewBox="0 0 667 340" aria-hidden="true">
      <g class="grid">
        <line x1="240" y1="60" x2="667" y2="60"/>
        <line x1="240" y1="130" x2="667" y2="130"/>
        <line x1="240" y1="200" x2="667" y2="200"/>
        <line x1="240" y1="270" x2="667" y2="270"/>
      </g>
      <g class="candle"><line x1="267" y1="180" x2="267" y2="300"/><rect x="260" y="200" width="14" height="70"/></g>
      <g class="candle candle--alt"><line x1="291" y1="150" x2="291" y2="270"/><rect x="284" y="170" width="14" height="80"/></g>
      <g class="candle"><line x1="315" y1="100" x2="315" y2="250"/><rect x="308" y="120" width="14" height="110"/></g>
      <g class="candle candle--alt"><line x1="339" y1="130" x2="339" y2="230"/><rect x="332" y="150" width="14" height="60"/></g>
      <g class="candle"><line x1="363" y1="70" x2="363" y2="230"/><rect x="356" y="90" width="14" height="120"/></g>
      <g class="candle"><line x1="387" y1="40" x2="387" y2="220"/><rect x="380" y="60" width="14" height="140"/></g>
      <g class="candle candle--alt"><line x1="411" y1="90" x2="411" y2="200"/><rect x="404" y="110" width="14" height="70"/></g>
      <g class="candle"><line x1="435" y1="20" x2="435" y2="180"/><rect x="428" y="40" width="14" height="120"/></g>
      <g class="candle candle--alt"><line x1="459" y1="60" x2="459" y2="190"/><rect x="452" y="80" width="14" height="90"/></g>
      <g class="candle"><line x1="483" y1="4" x2="483" y2="170"/><rect x="476" y="20" width="14" height="130"/></g>
      <g class="candle candle--alt"><line x1="507" y1="40" x2="507" y2="160"/><rect x="500" y="60" width="14" height="80"/></g>
      <g class="candle"><line x1="531" y1="0" x2="531" y2="140"/><rect x="524" y="10" width="14" height="110"/></g>
      <g class="candle candle--alt"><line x1="555" y1="30" x2="555" y2="140"/><rect x="548" y="50" width="14" height="70"/></g>
      <g class="candle"><line x1="579" y1="10" x2="579" y2="150"/><rect x="572" y="30" width="14" height="100"/></g>
      <g class="candle candle--alt"><line x1="603" y1="50" x2="603" y2="150"/><rect x="596" y="70" width="14" height="60"/></g>
      <g class="candle"><line x1="627" y1="0" x2="627" y2="125"/><rect x="620" y="15" width="14" height="90"/></g>
      <g class="candle candle--alt"><line x1="651" y1="20" x2="651" y2="130"/><rect x="644" y="40" width="14" height="70"/></g>
      <polyline class="trend" points="240,250 291,215 339,185 387,140 435,110 483,80 531,60 579,75 627,45 667,55"/>
    </svg>

    <div class="scene-industry" role="img" aria-label="Factory worker in a hard hat with a laptop beside yellow robotic arms on a manufacturing line"></div>

    <svg class="torn-band" viewBox="0 0 667 1000" aria-hidden="true">
      <polygon fill="var(--paper)" points="0,322 18,318 35,326 52,319 70,327 88,317 104,324 126,320 148,328 166,318 186,325 206,319 228,327 247,320 268,326 290,317 310,324 333,319 352,327 374,318 396,325 416,320 438,328 458,318 480,324 502,319 522,327 544,320 566,325 586,317 608,324 628,320 648,327 667,321 667,345 0,345"/>
      <polygon fill="var(--crimson)" points="0,330 20,334 41,328 60,336 82,330 102,337 124,331 146,336 168,329 190,335 212,330 234,337 256,329 278,334 300,328 322,335 344,330 366,337 388,331 410,336 432,329 454,334 476,330 498,337 520,331 542,335 564,329 586,334 608,330 630,336 650,331 667,334 667,700 0,700"/>
      <polygon fill="var(--paper)" points="0,668 22,664 44,671 66,662 88,669 110,661 132,668 154,664 176,672 198,663 220,669 242,661 264,667 286,664 308,671 330,662 352,668 374,661 396,667 418,664 440,672 462,663 484,669 506,661 528,668 550,664 572,671 594,663 616,669 640,662 667,668 667,680 0,680"/>
    </svg>

    <h1 class="cover-text title-line title-line--one">The Ledger and</h1>
    <p class="cover-text title-line title-line--two">The Lathe</p>
    <p class="cover-text subtitle">A Fresh Monetary Blueprint Built For<br>Modern Working Households</p>
    <p class="cover-text author">Daniel Reed Harlow</p>
  </div>
</div>
</body>
</html>
```